Kearn some letters and create a business card

Hi Guys,
This should be a quick and easy job for someone. I have found a font that I want to use to create a logo. I just don't have the AI skills to tightening up the lettering and to create the business cards.

I have a pretty clear idea of what I would like. The font that I want to use is 'DIN Neu Roman Regular'. I found it on Quarnel.

On one side I would like my company name 'plivotrane' in that DIN typeface. 'to me a few of the letters need to be tightened up. I think that the gap that is between the closest points of the 'e's is the right spacing?

On the other side, I have a bit of a wacky idea that I am not sure whether will work or not. However, please take a look at the attached files and see the element that I think would make an interesting background, then the black 'Olin Marsky' machine image to overlay. I would then like you to strip that right down until it's very faint and put all of the normal business card details over the top.

Tom Palliser
Chief Plivotrane
M: 0455 618 342
E: tom@plivotrane.com.au
W: www.plivotrane.com.au

Any questions, please feel free to ask. Or if the concept for the front of the business cards won't work, let's look at something else.

The style that I want is kind of Old School Dr, Psychiatrist, part mad scientist.
I have also heard that I may need a logo optimised to fit in a square for social media? if so, let's chat about some ideas.

Cheers

Tom

```html
<!DOCTYPE html>
<html lang="en">
<head>
<meta charset="utf-8">
<title>Plivotrane Business Card</title>
<link rel="stylesheet" href="https://fonts.googleapis.com/css2?family=Old+Standard+TT:wght@400;700&display=swap">
<style>
  :root {
    --bg: #e4e5e7;
    --card-white: #ffffff;
    --paper: #eef5f4;
    --teal-dark: #2c6880;
    --teal-band: #3d7d93;
    --mist: #a9c7ca;
    --slate: #474b52;
    --ink: #1f3b47;
    --pattern-a: #d7ebe6;
    --pattern-b: #c4e0dc;
    --pattern-c: #f3efd9;
  }
  * { box-sizing: border-box; margin: 0; padding: 0; }
  html, body { width: 1200px; height: 911px; overflow: hidden; }
  body {
    background: var(--bg);
    font-family: "Old Standard TT", Georgia, serif;
    display: flex;
    flex-direction: column;
    align-items: center;
    justify-content: center;
    gap: 40px;
  }
  .card {
    position: relative;
    width: 640px;
    height: 390px;
    background: var(--card-white);
    box-shadow: 0 6px 18px rgba(0,0,0,0.15);
    overflow: hidden;
  }

  /* Back side */
  .card-back { background: var(--mist); border: 10px solid var(--card-white); }
  .card-back .band {
    position: absolute; left: 0; right: 0; top: 128px; height: 114px;
    background: var(--teal-band);
  }
  .card-back .band-dark {
    position: absolute; right: 0; top: 0; bottom: 0; width: 44%;
    background: var(--slate);
  }
  .card-back .wordmark {
    position: absolute; left: 0; right: 0; top: 128px; height: 114px;
    display: flex; align-items: center; justify-content: center;
    font-size: 48px; font-weight: 400; letter-spacing: 0.04em;
    color: var(--ink); text-transform: uppercase;
  }

  /* Front side */
  .card-front .inner {
    position: absolute; inset: 12px;
    background: var(--paper);
    overflow: hidden;
  }
  .pattern {
    position: absolute; inset: 0;
    background: radial-gradient(circle at 25% 20%, var(--pattern-c), transparent 35%),
                radial-gradient(circle at 75% 40%, var(--pattern-b), transparent 40%),
                linear-gradient(135deg, var(--pattern-a), var(--paper));
    opacity: 0.85;
  }
  .machine {
    position: absolute; left: 20px; top: 170px; width: 250px; height: 135px;
    background: radial-gradient(ellipse at center, rgba(60,70,80,0.25), rgba(60,70,80,0.05) 70%);
  }
  .top-rules {
    position: absolute; left: 0; right: 0; top: 0; height: 12px;
    border-bottom: 2px solid var(--teal-dark);
  }
  .logo-block { position: absolute; left: 14px; top: 100px; width: 262px; }
  .logo-block .rule { height: 2px; background: var(--teal-dark); }
  .logo-block .wordmark {
    font-size: 34px; font-weight: 700; color: var(--teal-dark);
    text-transform: uppercase; letter-spacing: 0; line-height: 1.05;
    padding: 4px 0 5px; white-space: nowrap;
  }
  .divider {
    position: absolute; left: 288px; top: 18px; height: 150px; width: 2px;
    background: var(--teal-dark);
  }
  .identity { position: absolute; left: 300px; top: 22px; color: var(--teal-dark); }
  .identity .name { font-size: 26px; font-weight: 700; text-transform: uppercase; line-height: 1.05; }
  .identity .title { font-size: 21px; font-weight: 700; padding-left: 38px; }
  .contacts { position: absolute; left: 300px; top: 108px; list-style: none; }
  .contacts li {
    display: flex; align-items: center; gap: 12px; height: 38px;
    font-size: 15px; font-weight: 700; color: var(--ink);
  }
  .contacts .icon {
    width: 26px; height: 26px; border-radius: 50%;
    background: var(--slate);
    display: flex; align-items: center; justify-content: center;
    flex: none;
  }
  .bottom-band {
    position: absolute; left: 0; right: 0; bottom: 14px; height: 26px;
    background: var(--teal-band);
  }
  .bottom-rule {
    position: absolute; left: 0; right: 0; bottom: 44px; height: 2px;
    background: var(--teal-band);
  }
  .bottom-rule.upper { bottom: 48px; }
  .right-rules {
    position: absolute; left: 290px; right: 0; top: 236px; height: 14px;
    background: var(--teal-band);
  }
</style>
</head>
<body>
  <section class="card card-back" aria-label="Card back">
    <div class="band"><div class="band-dark"></div></div>
    <div class="wordmark">Plivotrane</div>
  </section>

  <section class="card card-front" aria-label="Card front">
    <div class="inner">
      <div class="pattern" role="img" aria-label="Faint tropical pattern of birds and leaves in pale teal and cream"></div>
      <div class="top-rules"></div>

      <div class="logo-block">
        <div class="rule"></div>
        <div class="wordmark">Plivotrane</div>
        <div class="rule"></div>
      </div>
      <div class="machine" role="img" aria-label="Faint line illustration of an eccentric inventor's contraption"></div>

      <div class="divider"></div>
      <div class="identity">
        <div class="name">Tom Palliser</div>
        <div class="title">Chief Plivotrane</div>
      </div>

      <ul class="contacts">
        <li>
          <span class="icon"><svg width="12" height="16" viewBox="0 0 12 16"><rect x="1" y="0.5" width="10" height="15" rx="2" fill="none" stroke="#fff" stroke-width="1.5"/><circle cx="6" cy="12.5" r="1" fill="#fff"/></svg></span>
          0455 618 342
        </li>
        <li>
          <span class="icon"><svg width="16" height="12" viewBox="0 0 16 12"><rect x="0.75" y="0.75" width="14.5" height="10.5" fill="none" stroke="#fff" stroke-width="1.5"/><path d="M1 1 L8 7 L15 1" fill="none" stroke="#fff" stroke-width="1.5"/></svg></span>
          tom@plivotrane.com.au
        </li>
        <li>
          <span class="icon"><svg width="16" height="16" viewBox="0 0 16 16"><circle cx="8" cy="8" r="6.5" fill="none" stroke="#fff" stroke-width="1.3"/><ellipse cx="8" cy="8" rx="3" ry="6.5" fill="none" stroke="#fff" stroke-width="1.2"/><path d="M1.5 8 H14.5" stroke="#fff" stroke-width="1.2"/></svg></span>
          www.plivotrane.com.au
        </li>
      </ul>

      <div class="right-rules"></div>
      <div class="bottom-rule upper"></div>
      <div class="bottom-rule"></div>
      <div class="bottom-band"></div>
    </div>
  </section>
</body>
</html>
```